Verpackungen für Klangschalenuhren
Zielgruppe
Unter der Marke 'Velmora' werden manufakturartig Klangschalenuhren in geringen Stückzahlen hergestellt. Produktionsort ist Deutschland, bis auf die Klangschalen.
Bei Klangschalenuhren wird mechanisch eine Klangschale angeschlagen.
Vorteile / Einsatz: Sanftes Aufwachen mit einer Klangschale / Ambiente: Hauch von Asien im Wohnbereich / Meditation & Wellness / Sitzungen, Behandlungen und Meetings
Zielgruppe:
„LOHAS“: kaufkräftig, bewusstes Leben, gesundheitsorientiert, natürliche/nachhaltige Produkte, Fairtrade/ethisches Handeln, authentisch. Selbständige (z.B. Therapeuten). Wellness.
Aufgabenstellung
Die Produktverpackung steht nicht im Verkaufsregal und muss daher kaum informative Elemente über das Produkt enthalten. Der Kunde sieht Verpackung beim Auspacken aus Versandkarton oder im Onlineshop.
WERTIG, NATÜRLICH, SCHLICHT. Kunde soll bei Empfang und Auspacken seines Produkts Freude empfinden.
Es gibt nur eine Verpackung für viele Modelle / Produktvarianten -> Produktfotos nicht geeignet.
Designelemente (Minimum):
Logo mit Claim „Der Klang der Zeit“. Mindestens auf Frontseite und Klappdeckel.
Ergänzen um ein stilisiertes Bild mit einer (angeschnittenen) Klangschale mit Klöppel
Handwerk aus Deutschland (mit oder ohne Symbol)
Adressdaten:
Velmora
Lindenstieg 9
64712 Eichenfeld-Rosbach
Deutschland
www.velmora-beispiel.de
Feld für Artikelaufkleber: 5 x 3 cm (bxh)
Zu bedruckender Karton:
Steckbodenschachtel
Größe 245 x 245 x 205 mm
aus Mikrowellpappe E-Welle innen braun
kaschiert mit GD2-Karton 230 g/qm
4/0-farbig bedruckt u. Dispersionsglanzlack

```html
<!DOCTYPE html>
<html lang="de">
<head>
<meta charset="utf-8">
<title>Velmora – Stanzform Steckbodenschachtel</title>
<link rel="stylesheet" href="https://fonts.googleapis.com/css2?family=Didact+Gothic&display=swap">
<style>
  :root {
    --page: #ffffff;
    --board: #fdf5e9;
    --ink: #333333;
    --fold: #222222;
    --cut: #1a9a3c;
    --accent: #f0c27a;
    --bowl: #f6dfb8;
    --sticker: #fcf8f2;
  }
  html, body {
    margin: 0;
    width: 1200px;
    height: 903px;
    overflow: hidden;
    background: var(--page);
  }
  .sheet {
    display: block;
    width: 1200px;
    height: 903px;
    font-family: "Didact Gothic", "Century Gothic", sans-serif;
  }
  .board { fill: var(--board); }
  .cut { fill: none; stroke: var(--cut); stroke-width: 2.4; stroke-linejoin: round; }
  .fold { fill: none; stroke: var(--fold); stroke-width: 2.4; }
  .brand { fill: var(--ink); font-weight: 400; }
  .claim { fill: var(--ink); }
  .subline { fill: var(--ink); letter-spacing: 1px; }
  .body-copy { fill: var(--ink); }
  .web { fill: var(--accent); letter-spacing: 1px; }
  .bowl-art { fill: var(--bowl); }
  .sticker-field { fill: var(--sticker); }
</style>
</head>
<body>
<svg class="sheet" viewBox="0 0 2212 1665" preserveAspectRatio="none" xmlns="http://www.w3.org/2000/svg">

  <!-- Markenname -->
  <text class="brand" x="145" y="205" font-size="135">Velmora</text>

  <!-- Karton -->
  <rect class="board" x="120" y="350" width="570" height="420"/>
  <rect class="board" x="120" y="762" width="2017" height="865"/>

  <!-- Schnittlinien -->
  <g class="cut">
    <path d="M180,405 L180,395 Q180,360 215,360 L625,360 Q656,360 656,395 L656,405"/>
    <path d="M178,405 L178,888 M658,405 L658,888"/>
    <path d="M178,405 L200,405 L203,408 M360,408 L363,404 L474,404 L477,408 M633,408 L636,405 L658,405"/>
    <path d="M178,892 L140,902 L140,1278 L178,1288"/>
    <path d="M658,795 L1108,795 L1128,868 L1135,875 L1135,890"/>
    <path d="M1135,890 L1318,890 L1318,870 Q1318,852 1336,852 L1418,852 Q1435,852 1435,870 L1435,890 L1618,890"/>
    <path d="M1318,890 L1318,928 M1435,890 L1435,928 M1357,890 A19,19 0 0 0 1396,890"/>
    <path d="M1618,890 L1618,875 L1626,868 L1645,795 L2094,795 L2094,1517"/>
    <path d="M178,1289 L298,1525 L298,1545 Q298,1562 316,1562 L520,1562 Q538,1562 538,1545 L538,1525 L658,1289"/>
    <path d="M658,1289 L658,1517 L895,1517 L895,1407 L1137,1289"/>
    <path d="M1137,1289 L1137,1562 L1256,1562 L1256,1524 L1498,1524 L1498,1562 L1616,1562 L1616,1289"/>
    <path d="M1616,1289 L1858,1407 L1858,1517 L2094,1517"/>
  </g>

  <!-- Rilllinien -->
  <g class="fold">
    <path d="M203,408 L360,408 M477,408 L633,408"/>
    <path d="M178,888 L658,888 M658,890 L1135,890 M1618,890 L2094,890"/>
    <path d="M1318,928 L1435,928"/>
    <path d="M178,1289 L2094,1289"/>
    <path d="M178,888 L178,1289 M658,888 L658,1289 M1137,890 L1137,1289 M1616,890 L1616,1289"/>
  </g>

  <!-- Klappdeckel -->
  <g text-anchor="middle">
    <text class="brand" x="420" y="545" font-size="60">Velmora</text>
    <text class="claim" x="420" y="618" font-size="29">Der Klang der Zeit</text>
    <text class="subline" x="420" y="643" font-size="13">HANDWERK  AUS  DEUTSCHLAND</text>
  </g>

  <!-- Frontseite -->
  <g text-anchor="middle">
    <text class="brand" x="418" y="1060" font-size="64">Velmora</text>
    <rect class="bowl-art" x="378" y="1120" width="82" height="68" rx="30" opacity="0.6" role="img" aria-label="Stilisierte Klangschale mit Klöppel in Goldtönen"/>
    <text class="claim" x="418" y="1223" font-size="29">Der Klang der Zeit</text>
    <text class="subline" x="418" y="1248" font-size="13">HANDWERK  AUS  DEUTSCHLAND</text>
  </g>

  <!-- Seite: Idee -->
  <g class="body-copy" text-anchor="middle" font-size="12">
    <text x="897" y="1164">Velmora ist die erste hochwertig gestaltete</text>
    <text x="897" y="1179">Klangschalenuhr der Welt.</text>
    <text x="897" y="1199">Sie entstand aus der Idee,</text>
    <text x="897" y="1214">westliche Uhrmacherkunst mit der Spiritualität</text>
    <text x="897" y="1229">fernöstlicher Klangschalen zu verbinden –</text>
    <text x="897" y="1249">um der Zeit erstmals in der Geschichte einen Klang zu geben.</text>
  </g>

  <!-- Rückseite: Adresse -->
  <g>
    <text class="brand" x="1185" y="1073" font-size="37">Velmora</text>
    <text class="claim" x="1185" y="1130" font-size="35">KLANGSCHALENUHR</text>
    <g class="body-copy" font-size="12">
      <text x="1185" y="1170">Velmora</text>
      <text x="1185" y="1189">Lindenstieg 9</text>
      <text x="1185" y="1203">64712 Eichenfeld-Rosbach</text>
      <text x="1185" y="1217">Deutschland</text>
    </g>
    <text class="web" x="1185" y="1249" font-size="26">www.velmora-beispiel.de</text>
    <rect class="sticker-field" x="1492" y="1190" width="96" height="58"/>
  </g>

  <!-- Seite: Material -->
  <g class="body-copy" text-anchor="middle" font-size="12">
    <text x="1855" y="1193">In Deutschland hergestelltes Unikat -</text>
    <text x="1855" y="1213">aus einem einzigen Stück Holz herausgearbeitet. Pures Holz.</text>
    <text x="1855" y="1234">Die Verwendung nachhaltig angebauter heimischer Hölzer</text>
    <text x="1855" y="1249">schonen die Umwelt und tragen zum Klimaschutz bei.</text>
  </g>
</svg>
</body>
</html>
```